Design for a newly formed Real Estate Management Company - Velmora Management

Background
Velmora Management is a Real Estate Company that manages properties for a small family business. I'd like to showcase the properties that I've acquired and turned around so they're performing well. This website will be a way for me to promote my business.

Different Sections
This website will help promote the work that I've been doing so it should include an About Us page. There should also be a page that goes through the different properties that we've managed and turned around. It would be great to have a design that allows me to visually show the different buildings that may be in various areas in a creative fashion. Finally, I need a section for a blog where I write about certain things prospective property owners should know about.

Design
http://www.dunrivet.com/ is a good example of the type of design I'm looking for. For the about us page, I'd like it to be able to show a portrait photo and a section to give some information about the person. I will be adding more people to the team so if there's a way to easily add photos and descriptions of new members, that would be great.

Target Market(s)

Third Party Real Estate Servicers (i.e. Insurance, Mortgage Brokers, Brokers)
Investors who are thinking to invest with us
Tenants who want to see how well we manage properties

Industry/Entity Type

Real Estate

Number of Pages Required

3 page

Requirements
Must have
• Integration of the logo into the design of the website would be a must. I'd like the design to flow together well and not be pages kind of stitched together. There should also be a way for me to easily add properties to the list. I should be able to monitor the people that join the website and obtain a login. It would be great to be able to edit and add things to the design so things aren't hardcoded.
Nice to have
• Allow tenants to write reviews of their experience at the property. Should not be anonymous, they would need to log in so at least their first name will show. Blog should also have log in so they may comment on the posts.

```html
<!DOCTYPE html>
<html lang="en">
<head>
<meta charset="utf-8">
<title>Velmora Management — Real Estate Management</title>
<link href="https://fonts.googleapis.com/css2?family=Open+Sans:wght@400;600;700&family=Lobster&display=swap" rel="stylesheet">
<style>
:root{
  --blue:#2f6fae;
  --blue-dark:#245a91;
  --blue-light:#3b82c4;
  --ink:#333;
  --muted:#666;
  --soft:#f4f3f4;
  --line:#e2e2e2;
  --dark:#1d1d1d;
  --darker:#121212;
  --white:#fff;
  --star:#f2b800;
}
*{box-sizing:border-box;margin:0;padding:0}
html,body{width:1200px;height:2469px;overflow:hidden}
body{font-family:"Open Sans",Arial,sans-serif;color:var(--ink);background:var(--white);position:relative}
.wrap{width:1002px;margin:0 auto;position:relative}

/* header */
.site-header{height:110px;border-top:3px solid var(--blue)}
.site-header .wrap{display:flex;align-items:center;height:107px}
.brand{display:flex;align-items:center;gap:12px;font-size:27px;font-weight:600;color:var(--blue-dark);letter-spacing:.5px}
.brand-mark{width:30px;height:30px;background:var(--blue-dark)}
.contact-bits{margin-left:auto;display:flex;gap:60px}
.contact-bit{display:flex;gap:14px;align-items:flex-start}
.contact-bit svg{width:22px;height:34px;fill:#333}
.contact-bit .label{font-size:12px;color:var(--blue-light)}
.contact-bit .value{font-size:14px;color:#333;line-height:1.35}
.contact-bit .value.small{font-size:12px}

/* nav */
.main-nav{height:55px;background:linear-gradient(#3a82c6,#2c6fb0)}
.main-nav ul{list-style:none;display:flex;justify-content:space-between;height:55px;width:1002px;margin:0 auto}
.main-nav li{color:#fff;font-size:13px;text-transform:uppercase;display:flex;align-items:center;justify-content:center;width:100px}
.main-nav li.active{background:#3a3a3a}
.main-nav li:last-child{justify-content:flex-end}

/* hero */
.hero{height:526px;position:relative;background:linear-gradient(180deg,#6f8a66 0%,#8e9a86 35%,#c9c2b3 55%,#6b7c4e 85%,#4f7a2f 100%);overflow:hidden}
.hero-title{position:absolute;top:232px;width:100%;text-align:center;color:#fff;font-size:44px;font-weight:700;letter-spacing:1px}
.hero-sub{position:absolute;top:290px;width:100%;text-align:center;color:#fff;font-size:26px;letter-spacing:1px}
.hero-arrow{position:absolute;top:197px;width:38px;height:38px;border-radius:50%;background:rgba(255,255,255,.45)}
.hero-arrow svg{width:38px;height:38px;fill:none;stroke:#444;stroke-width:3}
.hero-arrow.prev{left:34px}.hero-arrow.next{right:26px}

/* search */
.search-box{position:absolute;top:584px;left:99px;width:1002px;height:190px;background:#fff;box-shadow:0 3px 10px rgba(0,0,0,.18);padding:33px 20px 0}
.keyword{height:45px;border:1px solid #ccc;font-size:12px;color:#777;padding:13px 18px}
.filters{display:flex;margin-top:30px;align-items:flex-end}
.filter{margin-right:13px}
.filter .lbl{font-size:12px;color:#777;margin-bottom:8px}
.select{height:36px;border:1px solid #bbb;position:relative;font-size:11px;color:#555;padding:10px 8px;background:linear-gradient(#fff,#f1f1f1)}
.select::after{content:"";position:absolute;right:4px;top:8px;width:13px;height:18px;border:1px solid #999;background:#eee}
.btn-search{margin-left:auto;width:101px;height:40px;background:linear-gradient(#3a82c6,#2a6aa8);color:#fff;font-size:14px;font-weight:600;display:flex;align-items:center;justify-content:center;border-radius:2px}

/* welcome */
.welcome{height:428px;background:var(--soft);padding-top:124px;text-align:center;border-bottom:1px solid var(--line)}
.section-title{font-size:25px;color:var(--blue);text-transform:uppercase;font-weight:400}
.welcome .lead{font-size:14px;color:#555;line-height:23px;margin:16px auto 0;width:820px}
.welcome .body{font-size:11px;color:#666;line-height:24px;margin:12px auto 0;width:860px}
.welcome .actions{display:flex;justify-content:center;gap:12px;margin-top:37px}
.btn{height:46px;display:flex;align-items:center;justify-content:center;font-size:13px;text-transform:uppercase;border-radius:2px}
.btn-primary{width:168px;background:linear-gradient(#3a82c6,#2a6aa8);color:#fff}
.btn-outline{width:169px;border:2px solid #444;color:#333;background:#fff}

/* properties */
.properties{height:502px;position:relative}
.properties .section-title{position:absolute;top:40px;width:100%;text-align:center}
.pager{position:absolute;top:47px;right:99px;display:flex;gap:5px}
.pager span{width:24px;height:21px;background:#e6e6e6}
.cards{position:absolute;top:103px;left:99px;width:1002px;display:flex;justify-content:space-between}
.card{width:311px;text-align:center}
.card-photo{height:209px;position:relative;border:4px solid #fff;box-shadow:0 8px 8px -6px rgba(0,0,0,.3)}
.card-photo.p1{background:linear-gradient(180deg,#8fb4d8 0%,#4f6f6a 45%,#a9a9a0 70%,#6b8f3d 100%)}
.card-photo.p2{background:linear-gradient(180deg,#e4e6e5 0%,#cfc6b6 50%,#8e8f86 75%,#6e8460 100%)}
.card-photo.p3{background:linear-gradient(180deg,#8cb6e0 0%,#b9b4ac 40%,#e8e8e4 60%,#5e8f2f 100%)}
.tag-sale{position:absolute;top:39px;right:0;width:66px;height:31px;background:var(--blue-light);color:#fff;font-size:13px;display:flex;align-items:center;justify-content:center}
.tag-price{position:absolute;top:70px;right:0;width:72px;height:33px;background:#2b2b2b;color:#fff;font-size:14px;font-weight:600;display:flex;align-items:center;justify-content:center}
.card-name{font-size:14px;color:var(--blue);font-weight:600;margin-top:26px}
.card-desc{font-size:12px;color:#555;margin-top:5px;white-space:nowrap}
.card-meta{font-size:12px;color:#555;margin-top:6px;word-spacing:2px}
.btn-small{display:inline-flex;width:96px;height:38px;background:var(--blue);color:#fff;font-size:12px;text-transform:uppercase;align-items:center;justify-content:center;margin-top:17px;border-radius:2px}

/* blog */
.blog{height:288px;position:relative;border-top:1px solid var(--line);width:1002px;margin:0 auto}
.blog .section-title{position:absolute;top:43px;width:100%;text-align:center;font-size:20px}
.posts{position:absolute;top:101px;left:0;width:1002px;display:flex}
.post{display:flex;width:501px}
.post + .post{border-left:1px solid var(--line);padding-left:50px}
.post-photo{width:171px;height:134px;border:3px solid #fff;box-shadow:0 1px 5px rgba(0,0,0,.25);flex:none}
.post-photo.b1{background:linear-gradient(180deg,#f2f2f2 0%,#d9dbdd 55%,#8a5a48 100%)}
.post-photo.b2{background:linear-gradient(180deg,#4a7fc0 0%,#d8dde2 55%,#6d8f4d 100%)}
.post-text{margin-left:25px;width:270px}
.post-title{font-size:14px;font-weight:400;color:#333;white-space:nowrap}
.post-date{font-size:11px;color:var(--blue-light);margin-top:3px}
.post-excerpt{font-size:11px;color:#777;line-height:21px;margin-top:5px}
.post-foot{display:flex;align-items:center;gap:8px;margin-top:9px;font-size:11px;color:#888}
.stars{display:flex;gap:2px}
.stars svg{width:11px;height:11px;fill:var(--star)}
.stars svg.off{fill:#bbb}
.sep{width:1px;height:12px;background:#ccc}

/* offers */
.offers{height:290px;position:absolute;top:1909px;left:0;width:1200px;background:linear-gradient(180deg,#4d86c4 0%,#5b8fc7 50%,#4a79b0 100%);text-align:center;color:#fff}
.offers h2{font-family:"Lobster",cursive;font-weight:400;font-size:40px;margin-top:38px}
.offers p{font-size:13px;font-style:italic;line-height:26px;width:640px;margin:14px auto 0}
.btn-light{display:inline-flex;width:168px;height:44px;background:#f2f2f2;color:#444;font-size:12px;text-transform:uppercase;align-items:center;justify-content:center;margin-top:20px;border-radius:2px}

/* footer */
.site-footer{position:absolute;top:2199px;left:0;width:1200px;height:212px;background:var(--dark);color:#ddd}
.footer-cols{display:flex;width:1002px;margin:0 auto;padding-top:32px}
.footer-col h4{font-size:14px;font-weight:600;color:#fff;margin-bottom:20px}
.footer-col.links{width:151px}
.footer-col.contact{width:224px;border-right:1px solid #333;height:150px}
.footer-col.inquiry{width:248px;margin-left:48px;border-right:1px solid #333;height:150px}
.footer-col.news{margin-left:45px;width:286px}
.footer-col ul{list-style:none;font-size:12px;line-height:21px}
.contact li{display:flex;gap:10px}
.contact li svg{width:10px;height:12px;fill:#ccc;margin-top:5px;flex:none}
.contact li.indent{padding-left:20px}
.inquiry p{font-size:12px;color:#aaa;line-height:19px}
.btn-inquiry{display:inline-flex;width:89px;height:36px;background:var(--blue);color:#fff;font-size:12px;text-transform:uppercase;align-items:center;justify-content:center;margin-top:20px;border-radius:2px}
.news-item{display:flex;gap:8px;margin-bottom:18px}
.news-item .dot{width:5px;height:5px;border-radius:50%;background:var(--blue-light);margin-top:7px;flex:none}
.news-item p{font-size:12px;line-height:19px}
.news-item em{color:var(--blue-light);font-size:11px}
.bottom-bar{position:absolute;top:2411px;left:0;width:1200px;height:58px;background:var(--darker);color:#ccc;font-size:12px}
.bottom-bar .wrap{display:flex;align-items:center;height:58px}
.social{margin-left:auto;display:flex;align-items:center;gap:8px}
.social span.dot{width:27px;height:27px;border-radius:50%;border:2px solid #ccc}
.social .code{margin-left:38px;font-size:11px}
</style>
</head>
<body>

<header class="site-header">
  <div class="wrap">
    <div class="brand"><span class="brand-mark"></span>Velmora Management</div>
    <div class="contact-bits">
      <div class="contact-bit">
        <svg viewBox="0 0 22 34"><rect x="2" y="1" width="18" height="32" rx="3"/><rect x="5" y="5" width="12" height="21" fill="#fff"/><circle cx="11" cy="29.5" r="1.6" fill="#fff"/></svg>
        <div><div class="label">Phone:</div><div class="value">(555) 014-2290</div></div>
      </div>
      <div class="contact-bit">
        <svg viewBox="0 0 22 34"><path d="M11 1C5 1 1 5.5 1 11c0 7 10 20 10 20s10-13 10-20C21 5.5 17 1 11 1z"/><circle cx="11" cy="11" r="4" fill="#fff"/></svg>
        <div><div class="label">Location:</div><div class="value small">48 Harbor Lane, Suite 5<br>Street name, City-20915</div></div>
      </div>
    </div>
  </div>
</header>

<nav class="main-nav">
  <ul>
    <li class="active">Home</li><li>About Us</li><li>Services</li><li>Property</li><li>Blog</li><li>Videos</li><li>Contact</li>
  </ul>
</nav>

<section class="hero" role="img" aria-label="Photo of a two-storey clapboard house with a wide porch, surrounded by tall trees and a green lawn">
  <div class="hero-arrow prev"><svg viewBox="0 0 38 38"><path d="M22 11l-8 8 8 8"/></svg></div>
  <div class="hero-arrow next"><svg viewBox="0 0 38 38"><path d="M16 11l8 8-8 8"/></svg></div>
  <div class="hero-title">REAL ESTATE</div>
  <div class="hero-sub">MANAGEMENT</div>
</section>

<form class="search-box">
  <div class="keyword">Enter Keyword...</div>
  <div class="filters">
    <div class="filter"><div class="lbl">Property Type</div><div class="select" style="width:175px"></div></div>
    <div class="filter"><div class="lbl">Location</div><div class="select" style="width:90px"></div></div>
    <div class="filter"><div class="lbl">Select Status</div><div class="select" style="width:129px"></div></div>
    <div class="filter"><div class="lbl">Price</div><div class="select" style="width:127px">Min to Max</div></div>
    <div class="filter"><div class="lbl">Sqrt</div><div class="select" style="width:127px"></div></div>
    <div class="filter"><div class="lbl">Acr</div><div class="select" style="width:115px"></div></div>
    <div class="btn-search">SEARCH</div>
  </div>
</form>

<section class="welcome">
  <h2 class="section-title">Welcome to Velmora</h2>
  <p class="lead">Sed ut perspiciatis unde omnis iste natus error sit voluptatem accusantium doloremque laudantium, totam rem aperiam, eaque ipsa quae ab illo inventore veritatis et quasi architecto beatae...</p>
  <p class="body">Nemo enim ipsam voluptatem quia voluptas sit aspernatur aut odit aut fugit, sed quia consequuntur magni dolores eos qui ratione voluptatem sequi nesciunt. Neque porro quisquam est, qui dolorem ipsum quia dolor sit amet, consectetur, adipisci velit, sed quia non numquam eius modi tempora incidunt ut labore et dolore magnam aliquam quaerat voluptatem, ullam corporis suscipit laboriosam aliquid ex ea commodi consequatu...</p>
  <div class="actions"><span class="btn btn-primary">View More Info!</span><span class="btn btn-outline">Get Book Today!</span></div>
</section>

<section class="properties">
  <h2 class="section-title">Latest Properties</h2>
  <div class="pager"><span></span><span></span></div>
  <div class="cards">
    <article class="card">
      <div class="card-photo p1" role="img" aria-label="Photo of a blue two-storey family home with a driveway and pine trees"><span class="tag-sale">SALE</span><span class="tag-price">$129,000</span></div>
      <div class="card-name">PROPERTY NAME</div>
      <div class="card-desc">Lorem ipsum dolor sit amet, consectetur adipiscing.</div>
      <div class="card-meta">23 Acres &nbsp;| &nbsp;Lorem ipsum 2 &nbsp;| &nbsp;12,000 Sqrt</div>
      <span class="btn-small">Read More</span>
    </article>
    <article class="card">
      <div class="card-photo p2" role="img" aria-label="Photo of a modern white cube-shaped house with large windows"><span class="tag-sale">SALE</span><span class="tag-price">$129,000</span></div>
      <div class="card-name">PROPERTY NAME</div>
      <div class="card-desc">Lorem ipsum dolor sit amet, consectetur adipiscing.</div>
      <div class="card-meta">23 Acres &nbsp;| &nbsp;Lorem ipsum 2 &nbsp;| &nbsp;12,000 Sqrt</div>
      <span class="btn-small">Read More</span>
    </article>
    <article class="card">
      <div class="card-photo p3" role="img" aria-label="Photo of a contemporary stone and white villa with a palm tree and lawn"><span class="tag-sale">SALE</span><span class="tag-price">$129,000</span></div>
      <div class="card-name">PROPERTY NAME</div>
      <div class="card-desc">Lorem ipsum dolor sit amet, consectetur adipiscing.</div>
      <div class="card-meta">23 Acres &nbsp;| &nbsp;Lorem ipsum 2 &nbsp;| &nbsp;12,000 Sqrt</div>
      <span class="btn-small">Read More</span>
    </article>
  </div>
</section>

<section class="blog">
  <h2 class="section-title">Latestb Blog</h2>
  <div class="posts">
    <article class="post">
      <div class="post-photo b1" role="img" aria-label="Photo of a white modern house with a garage"></div>
      <div class="post-text">
        <h3 class="post-title">Accusantium doloremque laudantium</h3>
        <div class="post-date">Posted on Jan 15, 2016</div>
        <p class="post-excerpt">Tiit tortor elit, ullamcorper non odio sollicitudin, fermentum tristique nuncurabitur eu est orci. In entrance you will ipsum find..</p>
        <div class="post-foot">
          <span class="stars"><svg viewBox="0 0 10 10"><path d="M5 0l1.5 3.2 3.5.4-2.6 2.4.7 3.5L5 7.8 1.9 9.5l.7-3.5L0 3.6l3.5-.4z"/></svg><svg viewBox="0 0 10 10"><path d="M5 0l1.5 3.2 3.5.4-2.6 2.4.7 3.5L5 7.8 1.9 9.5l.7-3.5L0 3.6l3.5-.4z"/></svg><svg viewBox="0 0 10 10"><path d="M5 0l1.5 3.2 3.5.4-2.6 2.4.7 3.5L5 7.8 1.9 9.5l.7-3.5L0 3.6l3.5-.4z"/></svg><svg viewBox="0 0 10 10"><path d="M5 0l1.5 3.2 3.5.4-2.6 2.4.7 3.5L5 7.8 1.9 9.5l.7-3.5L0 3.6l3.5-.4z"/></svg><svg class="off" viewBox="0 0 10 10"><path d="M5 0l1.5 3.2 3.5.4-2.6 2.4.7 3.5L5 7.8 1.9 9.5l.7-3.5L0 3.6l3.5-.4z"/></svg></span>
          <span class="sep"></span><span>12 Reviews</span>
        </div>
      </div>
    </article>
    <article class="post">
      <div class="post-photo b2" role="img" aria-label="Photo of a white modernist house under a blue sky"></div>
      <div class="post-text">
        <h3 class="post-title">Accusantium doloremque laudantium</h3>
        <div class="post-date">Posted on Jan 15, 2016</div>
        <p class="post-excerpt">Tiit tortor elit, ullamcorper non odio sollicitudin, fermentum tristique nuncurabitur eu est orci. In entrance you will ipsum find..</p>
        <div class="post-foot">
          <span class="stars"><svg viewBox="0 0 10 10"><path d="M5 0l1.5 3.2 3.5.4-2.6 2.4.7 3.5L5 7.8 1.9 9.5l.7-3.5L0 3.6l3.5-.4z"/></svg><svg viewBox="0 0 10 10"><path d="M5 0l1.5 3.2 3.5.4-2.6 2.4.7 3.5L5 7.8 1.9 9.5l.7-3.5L0 3.6l3.5-.4z"/></svg><svg viewBox="0 0 10 10"><path d="M5 0l1.5 3.2 3.5.4-2.6 2.4.7 3.5L5 7.8 1.9 9.5l.7-3.5L0 3.6l3.5-.4z"/></svg><svg viewBox="0 0 10 10"><path d="M5 0l1.5 3.2 3.5.4-2.6 2.4.7 3.5L5 7.8 1.9 9.5l.7-3.5L0 3.6l3.5-.4z"/></svg><svg class="off" viewBox="0 0 10 10"><path d="M5 0l1.5 3.2 3.5.4-2.6 2.4.7 3.5L5 7.8 1.9 9.5l.7-3.5L0 3.6l3.5-.4z"/></svg></span>
          <span class="sep"></span><span>12 Reviews</span>
        </div>
      </div>
    </article>
  </div>
</section>

<section class="offers" role="img" aria-label="Blurred blue-tinted photo of a family house behind the offer text">
  <h2>Special Offers for Small family</h2>
  <p>Sed tortor elit, ullamcorper non odio sollicitudi fermentum tristique nuncurabitur eu est orciNemo enim ipsam voluptatem quia voluptas sit aspernatur. In sodalesdui eget tempor consequat The standard room lorem. qui dolorem ipsum quia dolor sit amet..</p>
  <span class="btn-light">View More Info!</span>
</section>

<footer class="site-footer">
  <div class="footer-cols">
    <div class="footer-col links">
      <h4>LINKS</h4>
      <ul><li>Home</li><li>About us</li><li>Services</li><li>Properties</li><li>Blog</li><li>Contact us</li></ul>
    </div>
    <div class="footer-col contact">
      <h4>CONTACT US</h4>
      <ul>
        <li><svg viewBox="0 0 10 12"><path d="M5 0C2.2 0 0 2.2 0 5c0 3.5 5 7 5 7s5-3.5 5-7c0-2.8-2.2-5-5-5z"/></svg>312 Velmora Management</li>
        <li class="indent">Elm Row, City name-7381</li>
        <li><svg viewBox="0 0 10 12"><rect x="2" y="0" width="6" height="12" rx="1"/></svg>Phone: 555-014-2290</li>
        <li><svg viewBox="0 0 10 12"><rect x="0" y="3" width="10" height="8" rx="1"/><rect x="2" y="0" width="6" height="4"/></svg>Fax: 555-018-3374</li>
        <li><svg viewBox="0 0 10 12"><rect x="0" y="3" width="10" height="7"/></svg>Email: info@velmora.com</li>
      </ul>
    </div>
    <div class="footer-col inquiry">
      <h4>INQUIRY HERE</h4>
      <p>Sed ut perspiciatis unde omnis iste natus error sit voluptatem accusanti doloremque la udantium.</p>
      <span class="btn-inquiry">Inquiry</span>
    </div>
    <div class="footer-col news">
      <h4>LATEST NEWS</h4>
      <div class="news-item"><span class="dot"></span><p>Sed ut perspiciatis unde &nbsp;enim ipsam voluptatem<br><em>Posted January 30, 2016 at 11:06 pm</em></p></div>
      <div class="news-item"><span class="dot"></span><p>Sed ut perspiciatis unde &nbsp;enim ipsam voluptatem<br><em>Posted January 30, 2016 at 11:06 pm</em></p></div>
    </div>
  </div>
</footer>

<div class="bottom-bar">
  <div class="wrap">
    <span>Copyright © 2016 &nbsp;Velmora Management | Sitemap</span>
    <div class="social">Connect With Us: <span class="dot"></span><span class="dot"></span><span class="dot"></span><span class="dot"></span><span class="code">C11</span></div>
  </div>
</div>

</body>
</html>
```